Menu for burgers the restaurant will be called 'THE LANTERN'

something special that reflects the image of a relaxed and friendly bar.
you will find a picture of a menu for inspiration.
Some examples uploaded

Target Market(s)

all categories who search for simple and funny bar for watching football

Requirements
Must have
• some funny emoticons
font style - like the picture of the menu uploaded
if you can do the same menu it will be perfect !!! the cow at the background etc...
Nice to have
• black font style and colorful wall (not too much) simple and elegant
Should not have
• a lot of colours
serious emoticons

```html
<!DOCTYPE html>
<html lang="fr">
<head>
<meta charset="utf-8">
<title>The Lantern – Menu Burgers</title>
<link rel="stylesheet" href="https://fonts.googleapis.com/css2?family=Bebas+Neue&family=Oswald:wght@400;500&display=swap">
<style>
:root{
  --ink:#1d1a15;
  --paper:#d8cba9;
  --paper-light:#e6dcc0;
  --paper-dark:#c4b48e;
  --backdrop:#f2f2f2;
  --placeholder:#2a2621;
}
*{box-sizing:border-box;margin:0;padding:0}
html,body{width:1200px;height:1200px;overflow:hidden;background:var(--backdrop)}
.menu-sheet{
  position:absolute;left:40px;top:205px;width:1120px;height:789px;
  background:
    radial-gradient(ellipse at 30% 40%,var(--paper-light) 0%,transparent 55%),
    radial-gradient(ellipse at 80% 75%,var(--paper-dark) 0%,transparent 60%),
    var(--paper);
  color:var(--ink);
  font-family:"Oswald",sans-serif;
}
.block{position:absolute}
.section-title{
  position:absolute;font-family:"Bebas Neue",sans-serif;font-size:44px;line-height:1;font-weight:400;
  writing-mode:vertical-rl;transform:rotate(180deg);letter-spacing:1px;white-space:nowrap;
}
.section-title.small{font-size:30px}
.section-title .sub{font-size:17px;display:inline-block}
.price-table{border-collapse:collapse;width:100%;table-layout:fixed}
.price-table td,.price-table th{border:1.5px solid var(--ink)}
.price-table th{font-family:"Bebas Neue",sans-serif;font-weight:400;font-size:17px;height:24px;text-align:center}
.price-table th.blank{border-top:none;border-left:none}
.item-name td{font-family:"Bebas Neue",sans-serif;font-size:22px;line-height:.95;height:33px;padding:4px 4px 1px;white-space:nowrap}
.item-name td.wrap{white-space:normal}
.item-name td.price{text-align:center;font-size:21px;padding:4px 0 0}
.item-desc td{font-size:8.5px;line-height:1.35;text-transform:uppercase;padding:3px 4px 4px;height:34px;vertical-align:top;letter-spacing:.2px}
.item-desc .alert{font-family:"Bebas Neue",sans-serif;font-size:15px;letter-spacing:.4px;display:block;line-height:1.1}
.item-name td .tiny{font-size:12px}
.extra-title{position:absolute;font-family:"Bebas Neue",sans-serif;font-size:26px;line-height:1;text-align:center;width:209px;font-weight:400}
.extra-table td{font-size:10px;text-transform:uppercase;padding:3px 5px;height:23px}
.extra-table td.price{font-family:"Bebas Neue",sans-serif;font-size:19px;text-align:center;width:42px}
.halal{position:absolute;font-family:"Bebas Neue",sans-serif;font-size:26px;left:348px;top:728px}
.brand-seal{position:absolute;left:593px;top:56px;width:174px;height:174px;border:3px solid var(--ink);border-radius:50%;display:flex;align-items:center;justify-content:center}
.brand-name{font-family:"Bebas Neue",sans-serif;font-size:42px;line-height:.9;text-align:center}
.legend-bubble{position:absolute;left:589px;top:259px;width:88px;height:88px;border-radius:50%;background:var(--ink);color:var(--paper-light);font-family:"Bebas Neue",sans-serif;font-size:18px;line-height:1.15;display:flex;flex-direction:column;justify-content:center;align-items:center}
.icon-fill{position:absolute;background:var(--placeholder);border-radius:6px}
.bull-head{position:absolute;left:673px;top:309px;width:114px;height:147px;background:radial-gradient(ellipse at 50% 45%,#6b6254 0%,#3a342c 70%,transparent 72%)}
.stars{position:absolute;left:630px;top:474px;font-size:15px;letter-spacing:5px;white-space:nowrap;line-height:1}
.note{position:absolute;font-size:8px;text-transform:uppercase;text-align:center;line-height:1.3}
.compact .item-name td{height:29px;font-size:22px}
.compact .item-name td.price{font-size:20px}
.sides td{font-size:10px;text-transform:uppercase;padding:2px 5px;height:25px;font-weight:500}
.sides td.price{font-family:"Bebas Neue",sans-serif;font-size:19px;text-align:center;width:44px;font-weight:400}
</style>
</head>
<body>
<main class="menu-sheet">

  <!-- Beef burgers -->
  <h2 class="section-title" style="left:22px;top:18px;height:320px;text-align:center">BURGERS BŒUF</h2>
  <div class="icon-fill" role="img" aria-label="Small cow silhouette icon" style="left:103px;top:16px;width:50px;height:30px"></div>
  <div class="block" style="left:91px;top:29px;width:208px">
    <table class="price-table">
      <colgroup><col><col style="width:40px"><col style="width:40px"></colgroup>
      <tr><th class="blank"></th><th>B</th><th>M</th></tr>
      <tr class="item-name"><td>BIG BEEF</td><td class="price">8.9</td><td class="price">13.9</td></tr>
      <tr class="item-desc"><td colspan="3">Ketchup, cornichons, oignons caramélisés, tomate, salade, sauce maison</td></tr>
      <tr class="item-name"><td>BIG CHEESE</td><td class="price">10.9</td><td class="price">15.9</td></tr>
      <tr class="item-desc"><td colspan="3">Cheddar, ketchup, cornichons, oignons caramélisés, tomate, salade, sauce maison</td></tr>
      <tr class="item-name"><td>MEXICANA BEEF</td><td class="price">12.9</td><td class="price">17.9</td></tr>
      <tr class="item-desc"><td colspan="3">Guacamole, ketchup, oignons caramélisés, salade, sauce maison</td></tr>
      <tr class="item-name"><td><span class="tiny">THE</span>SPECIAL ONE</td><td class="price">12.9</td><td class="price">17.9</td></tr>
      <tr class="item-desc"><td colspan="3">Purée de tomate maison, œuf, huile d'olive, persil, sauce maison</td></tr>
      <tr class="item-name"><td class="wrap">RED HOT CHILI<br>BURGER</td><td class="price">12.9</td><td class="price">17.9</td></tr>
      <tr class="item-desc"><td colspan="3">Cheddar, oignons caramélisés, tomate, salade, sauce piquante maison</td></tr>
    </table>
  </div>

  <div class="icon-fill" role="img" aria-label="Small cow silhouette icon" style="left:350px;top:16px;width:50px;height:30px"></div>
  <div class="block" style="left:325px;top:29px;width:209px">
    <table class="price-table">
      <colgroup><col><col style="width:40px"><col style="width:40px"></colgroup>
      <tr><th class="blank"></th><th>B</th><th>M</th></tr>
      <tr class="item-name"><td>DIE SCHWEIZER</td><td class="price">12.9</td><td class="price">17.9</td></tr>
      <tr class="item-desc"><td colspan="3">Fromage à raclette aux poivres, cornichon, salade, oignons caramélisés, sauce moutarde</td></tr>
      <tr class="item-name"><td>THE GOAT</td><td class="price">13.9</td><td class="price">18.9</td></tr>
      <tr class="item-desc"><td colspan="3">Bacon, rondelle de chèvre, miel, oignons caramélisés, salade, sauce maison</td></tr>
      <tr class="item-name"><td>EL MATADOR</td><td class="price">12.9</td><td class="price">17.9</td></tr>
      <tr class="item-desc"><td colspan="3">Chorizo, jalapeños, tomate, salade, sauce aïoli maison</td></tr>
      <tr class="item-name"><td>SMOKEY BEEF</td><td class="price">12.9</td><td class="price">17.9</td></tr>
      <tr class="item-desc"><td colspan="3">Bacon, cheddar, oignons caramélisés, onion rings, salade, sauce BBQ</td></tr>
    </table>
  </div>

  <svg class="block" style="left:373px;top:352px" width="100" height="40" viewBox="0 0 100 40" aria-hidden="true">
    <g fill="var(--ink)">
      <polygon points="0,4 12,4 26,20 12,36 0,36 14,20"/>
      <polygon points="24,4 36,4 50,20 36,36 24,36 38,20"/>
      <polygon points="48,4 60,4 74,20 60,36 48,36 62,20"/>
      <polygon points="72,4 84,4 98,20 84,36 72,36 86,20"/>
    </g>
  </svg>

  <!-- Chicken burgers -->
  <h2 class="section-title" style="left:22px;top:424px;height:350px;text-align:center">BURGERS POULET</h2>
  <div class="icon-fill" role="img" aria-label="Small chicken and leaf icons" style="left:103px;top:420px;width:105px;height:32px"></div>
  <div class="block" style="left:91px;top:433px;width:208px">
    <table class="price-table">
      <colgroup><col><col style="width:40px"><col style="width:40px"></colgroup>
      <tr><th class="blank"></th><th>B</th><th>M</th></tr>
      <tr class="item-name"><td>THE CRISPY</td><td class="price">8.9</td><td class="price">13.9</td></tr>
      <tr class="item-desc"><td colspan="3">Ketchup, cornichons, oignons caramélisés, tomate, salade, sauce maison</td></tr>
      <tr class="item-name"><td class="wrap">MEXICANA<br>CHICKEN</td><td class="price">12.9</td><td class="price">17.9</td></tr>
      <tr class="item-desc"><td colspan="3">Cheddar, ketchup, cornichons, oignons caramélisés, salade, sauce maison</td></tr>
      <tr class="item-name"><td>GRECOS</td><td class="price">8.9</td><td class="price">13.9</td></tr>
      <tr class="item-desc"><td colspan="3">Ketchup, cornichons, oignons caramélisés, tomate, salade, sauce piquante maison</td></tr>
      <tr class="item-name"><td class="wrap">BURGER<br>VEGGIE</td><td class="price">12.9</td><td class="price">17.9</td></tr>
      <tr class="item-desc"><td colspan="3">Cheddar, ketchup, cornichons, oignons caramélisés, tomate, salade, sauce maison</td></tr>
    </table>
  </div>

  <!-- Extras -->
  <h3 class="extra-title" style="left:325px;top:424px">SUPPLÉMENTS VIANDES</h3>
  <div class="block" style="left:325px;top:454px;width:209px">
    <table class="price-table extra-table">
      <tr><td>Bœuf (160g)</td><td class="price">4.5</td></tr>
      <tr><td>Poulet (120g)</td><td class="price">4</td></tr>
    </table>
  </div>
  <h3 class="extra-title" style="left:325px;top:526px;text-align:right">TOPPINGS</h3>
  <div class="block" style="left:325px;top:558px;width:209px">
    <table class="price-table extra-table">
      <tr><td style="font-size:8.5px;line-height:1.3">Fromage, œuf, bacon, chorizo, guacamole, oignons caramélisés</td><td class="price">2</td></tr>
    </table>
  </div>
  <h3 class="extra-title" style="left:325px;top:602px;text-align:right">UPGRADES</h3>
  <div class="block" style="left:325px;top:633px;width:209px">
    <table class="price-table extra-table">
      <tr><td>Patates douces / potatoes</td><td class="price">+2</td></tr>
      <tr><td>Milkshake classique</td><td class="price">+3</td></tr>
      <tr><td>Bière</td><td class="price">+3</td></tr>
    </table>
  </div>
  <p class="halal">HALAL SUR DEMANDE</p>

  <!-- Centre -->
  <div class="brand-seal"><span class="brand-name">THE<br>LANTERN</span></div>
  <div class="legend-bubble"><span>B = BURGER</span><span>M = MENU</span></div>
  <div class="bull-head" role="img" aria-label="Engraved illustration of a bull's head"></div>

  <!-- Competition burgers -->
  <h2 class="section-title small" style="left:803px;top:29px;height:275px;text-align:center">COMPETITION BURGERS<br><span class="sub">DEMANDEZ LES 'AVANT 20MIN'</span></h2>
  <div class="icon-fill" role="img" aria-label="Small moustache icon" style="left:842px;top:33px;width:34px;height:14px;border-radius:8px"></div>
  <div class="block" style="left:880px;top:25px;width:213px">
    <table class="price-table">
      <colgroup><col><col style="width:40px"></colgroup>
      <tr class="item-name"><td class="wrap">THE MONSTER<br>'BIG MOUTH BURGER'</td><td class="price">39.9</td></tr>
      <tr class="item-desc"><td colspan="2"><span class="alert">SI FINI EN 15 MIN -&gt; DESSERT OFFERT</span>Triple beef, triple cheddar, cornichons, salade, tomate, sauce maison, double ration de frites et boisson</td></tr>
    </table>
  </div>
  <div class="block" style="left:880px;top:165px;width:213px">
    <table class="price-table">
      <colgroup><col><col style="width:40px"></colgroup>
      <tr class="item-name"><td class="wrap">MOVING MOUNTAIN<br>BURGER</td><td class="price">69.9</td></tr>
      <tr class="item-desc"><td colspan="2"><span class="alert">SI FINI EN 20 MIN -&gt; CHICHA OFFERTE</span>Quintuple beef, quintuple cheddar, cornichons, onion rings, salade, tomate, sauce maison, frites cheddar et boisson</td></tr>
    </table>
  </div>

  <!-- Salads -->
  <h2 class="section-title small" style="left:826px;top:318px;height:140px;text-align:center">SALADES</h2>
  <div class="icon-fill" role="img" aria-label="Small leaf icon" style="left:832px;top:322px;width:16px;height:16px;border-radius:50%"></div>
  <div class="block" style="left:880px;top:319px;width:213px">
    <table class="price-table">
      <colgroup><col><col style="width:40px"></colgroup>
      <tr class="item-name"><td>CHICKEN SALAD</td><td class="price">16.9</td></tr>
      <tr class="item-desc"><td colspan="2">Filet de poulet, salade, tomate, gruyère AOP, onion rings, sauce au citron vert</td></tr>
      <tr class="item-name"><td>HAWAII</td><td class="price">17.9</td></tr>
      <tr class="item-desc"><td colspan="2">Crevettes roses, ananas, avocats, concombre, coriandre, feuilles de salade, sauce cocktails</td></tr>
    </table>
  </div>

  <p class="stars">★★★★★★★★★★★★★★★★★</p>

  <!-- Student menu -->
  <h2 class="section-title small" style="left:630px;top:496px;height:158px;text-align:center">MENU ETUDIANT</h2>
  <div class="block compact" style="left:671px;top:502px;width:137px">
    <table class="price-table">
      <colgroup><col><col style="width:40px"></colgroup>
      <tr class="item-name"><td>BIG BEEF</td><td class="price">11.9</td></tr>
      <tr class="item-name"><td>BIG CHEESE</td><td class="price">12.9</td></tr>
      <tr class="item-name"><td>THE CRISPY</td><td class="price">12.9</td></tr>
      <tr class="item-name"><td>THE VEGGIE</td><td class="price">12.9</td></tr>
    </table>
  </div>
  <p class="note" style="left:664px;top:628px;width:152px">(avec boisson sans alcool et frites)<br>un menu par carte d'étudiant</p>

  <!-- Kids menu -->
  <h2 class="section-title small" style="left:840px;top:496px;height:158px;text-align:center">MENU ENFANT</h2>
  <div class="block compact" style="left:880px;top:488px;width:213px">
    <table class="price-table">
      <colgroup><col><col style="width:40px"><col style="width:40px"></colgroup>
      <tr><th class="blank"></th><th>B</th><th>M</th></tr>
      <tr class="item-name"><td>JUNIOR BEEF</td><td class="price">6.9</td><td class="price">10.9</td></tr>
      <tr class="item-name"><td>JUNIOR CHEESE</td><td class="price">7.9</td><td class="price">11.9</td></tr>
      <tr class="item-name"><td>JUNIOR CRISPY</td><td class="price">7.9</td><td class="price">11.9</td></tr>
      <tr class="item-name"><td>JUNIOR VEGGIE</td><td class="price">7.9</td><td class="price">11.9</td></tr>
    </table>
  </div>
  <p class="note" style="left:935px;top:636px;width:160px">(avec boisson sans alcool et frites)</p>

  <!-- Sides -->
  <div class="icon-fill" role="img" aria-label="Small diamond icon" style="left:612px;top:706px;width:24px;height:20px;border-radius:2px"></div>
  <div class="block" style="left:671px;top:688px;width:196px">
    <table class="price-table sides">
      <tr><td>Patatas bravas</td><td class="price">8.9</td></tr>
      <tr><td>Filets de poulets 'tenders'</td><td class="price">12.9</td></tr>
      <tr><td>Beef chili cheese fries</td><td class="price">14.9</td></tr>
    </table>
  </div>
  <div class="block" style="left:880px;top:663px;width:213px">
    <table class="price-table sides">
      <tr><td>Onion rings (4 pièces)</td><td class="price">4.9</td></tr>
      <tr><td>Frites</td><td class="price">4.9</td></tr>
      <tr><td>Patates douces</td><td class="price">5.9</td></tr>
      <tr><td>Potatoes</td><td class="price">5.9</td></tr>
    </table>
  </div>

</main>
</body>
</html>
```